Car Detailing product label for 750ML Clear Bottle

I need a label for various product with differente color for each products but in the same size bottle each time. It's only for our purpose no commercial application. I need a template with differente color but same design. The name for product it's : Brisk Harbor. We dont have any logo because it's only for us. We like like car silhouette in the logo or in background or something like that.

And for the product we have many like : APC Cleaner, Drying Aid, Wheel Cleaner and some other.

Font styles to use
Serif
Sans Serif

```html
<!DOCTYPE html>
<html lang="en">
<head>
<meta charset="utf-8">
<title>Brisk Harbor – Product Label Range</title>
<link rel="stylesheet" href="https://fonts.googleapis.com/css2?family=Lato:wght@400;700;900&family=Russo+One&display=swap">
<style>
  :root {
    --page: #ffffff;
    --body-dark: #0b0b0c;
    --body-mid: #1c1d20;
    --chrome-light: #e6e7ea;
    --chrome-dark: #55575c;
    --ink-light: #ffffff;
    --red: #e30613;
    --red-deep: #8d0008;
    --red-soft: #ffb3b8;
    --purple: #7a00d8;
    --purple-deep: #3b0078;
    --purple-soft: #d6a8ff;
    --blue: #0a6fe8;
    --blue-deep: #053d8a;
    --blue-soft: #a9d1ff;
  }
  * { box-sizing: border-box; margin: 0; padding: 0; }
  html, body {
    width: 1200px; height: 2319px; overflow: hidden;
    background: var(--page);
  }
  .label-sheet {
    position: relative; width: 1200px; height: 2319px;
    display: flex; flex-direction: column; align-items: center;
    gap: 36px; padding-top: 40px;
  }
  .label {
    position: relative; width: 268px; height: 722px; overflow: hidden;
    background: radial-gradient(ellipse at 50% 45%, var(--body-mid) 0%, var(--body-dark) 70%);
    font-family: "Lato", sans-serif;
  }
  .label--apc { --accent: var(--red); --accent-deep: var(--red-deep); --accent-soft: var(--red-soft); }
  .label--drying { --accent: var(--purple); --accent-deep: var(--purple-deep); --accent-soft: var(--purple-soft); }
  .label--wheel { --accent: var(--blue); --accent-deep: var(--blue-deep); --accent-soft: var(--blue-soft); }

  .label__top-band {
    position: absolute; left: 0; top: 0; width: 100%; height: 63px;
    background: var(--accent);
    display: flex; align-items: flex-end; justify-content: center; padding-bottom: 10px;
  }
  .label__tagline {
    font-size: 10px; font-weight: 700; letter-spacing: 3.4px;
    color: var(--accent-soft);
  }
  .label__chrome-rule {
    position: absolute; left: 0; top: 64px; width: 100%; height: 7px;
    background: linear-gradient(180deg, var(--chrome-dark), var(--chrome-light) 45%, var(--chrome-dark));
  }
  .label__brand {
    position: absolute; left: 0; top: 132px; width: 100%;
    display: flex; align-items: center; justify-content: center; gap: 8px;
  }
  .label__brand-dot {
    width: 12px; height: 12px; border-radius: 50%; background: var(--ink-light);
  }
  .label__brand-name {
    font-size: 25px; font-weight: 900; letter-spacing: 1px; color: var(--ink-light);
    text-transform: uppercase;
  }
  .label__claim {
    position: absolute; left: 0; top: 285px; width: 100%;
    display: flex; flex-direction: column; align-items: center;
    transform: rotate(-7deg);
  }
  .label__product {
    font-family: "Russo One", sans-serif; text-transform: uppercase;
    line-height: 0.92; text-align: center;
    background: linear-gradient(180deg, var(--accent) 0%, var(--accent-deep) 100%);
    -webkit-background-clip: text; background-clip: text; color: transparent;
  }
  .label__product-line { display: block; }
  .label--apc .label__product-line--a { font-size: 68px; }
  .label--apc .label__product-line--b { font-size: 30px; }
  .label--drying .label__product-line--a { font-size: 44px; }
  .label--drying .label__product-line--b { font-size: 58px; }
  .label--wheel .label__product-line--a { font-size: 44px; }
  .label--wheel .label__product-line--b { font-size: 42px; }
  .label__subline {
    margin-top: 6px; font-family: "Russo One", sans-serif;
    font-size: 12px; color: var(--ink-light); letter-spacing: 0.5px;
  }
  .label__pill {
    margin-top: 6px; padding: 4px 12px;
    background: linear-gradient(90deg, var(--accent-deep), var(--accent));
    font-family: "Russo One", sans-serif; font-size: 8px; letter-spacing: 1px;
    color: var(--ink-light);
  }
  .label__lower-chrome {
    position: absolute; left: 0; bottom: 0; width: 100%; height: 182px;
    background: linear-gradient(180deg, var(--chrome-light), var(--chrome-dark));
    clip-path: polygon(0 22%, 100% 0, 100% 100%, 0 100%);
  }
  .label__lower-band {
    position: absolute; left: 0; bottom: 0; width: 100%; height: 175px;
    background: linear-gradient(180deg, var(--accent) 0%, var(--accent) 100%);
    clip-path: polygon(0 23%, 100% 0, 100% 100%, 0 100%);
    display: flex; align-items: flex-end; justify-content: center; padding-bottom: 24px;
  }
  .label__volume {
    font-size: 17px; font-weight: 700; color: var(--ink-light);
  }
</style>
</head>
<body>
<main class="label-sheet">

  <article class="label label--apc">
    <header class="label__top-band"><span class="label__tagline">PREMIUM QUALITY</span></header>
    <div class="label__chrome-rule"></div>
    <div class="label__brand"><span class="label__brand-dot"></span><span class="label__brand-name">Brisk Harbor</span></div>
    <div class="label__claim">
      <h2 class="label__product"><span class="label__product-line label__product-line--a">APC</span><span class="label__product-line label__product-line--b">Cleaner</span></h2>
      <p class="label__subline">LOREM IPSUM DOLOR SIT AMET</p>
      <p class="label__pill">LOREM IPSUM DOLOR</p>
    </div>
    <div class="label__lower-chrome"></div>
    <footer class="label__lower-band"><span class="label__volume">750ML</span></footer>
  </article>

  <article class="label label--drying">
    <header class="label__top-band"><span class="label__tagline">PREMIUM QUALITY</span></header>
    <div class="label__chrome-rule"></div>
    <div class="label__brand"><span class="label__brand-dot"></span><span class="label__brand-name">Brisk Harbor</span></div>
    <div class="label__claim">
      <h2 class="label__product"><span class="label__product-line label__product-line--a">Drying</span><span class="label__product-line label__product-line--b">Aid</span></h2>
      <p class="label__subline">LOREM IPSUM DOLOR SIT AMET</p>
      <p class="label__pill">LOREM IPSUM DOLOR</p>
    </div>
    <div class="label__lower-chrome"></div>
    <footer class="label__lower-band"><span class="label__volume">750ML</span></footer>
  </article>

  <article class="label label--wheel">
    <header class="label__top-band"><span class="label__tagline">PREMIUM QUALITY</span></header>
    <div class="label__chrome-rule"></div>
    <div class="label__brand"><span class="label__brand-dot"></span><span class="label__brand-name">Brisk Harbor</span></div>
    <div class="label__claim">
      <h2 class="label__product"><span class="label__product-line label__product-line--a">Wheel</span><span class="label__product-line label__product-line--b">Cleaner</span></h2>
      <p class="label__subline">LOREM IPSUM DOLOR SIT AMET</p>
      <p class="label__pill">LOREM IPSUM DOLOR</p>
    </div>
    <div class="label__lower-chrome"></div>
    <footer class="label__lower-band"><span class="label__volume">750ML</span></footer>
  </article>

</main>
</body>
</html>
```